Criação de Folder para Horizonte & Veredas
A empresa queria:
" Atendemos os clientes de forma consultiva, procurando no mercado as tecnologias mais adequadas para a otimização e estabilidade de redes corporativas. Somos parceiros homologados dos principais fabricantes do mercado, além de mantermos parcerias estratégicas para complementar nossas soluções com todas as competências necessárias. "

```html
<!DOCTYPE html>
<html lang="pt-BR">
<head>
<meta charset="utf-8">
<title>Folder Horizonte &amp; Veredas</title>
<link rel="stylesheet" href="https://fonts.googleapis.com/css2?family=Open+Sans:wght@400;600;700;800&display=swap">
<style>
:root{
  --teal:#2aa3b9;
  --teal-dark:#1f8598;
  --ink:#1b2127;
  --text:#5e6870;
  --muted:#a9b1b7;
  --paper:#ffffff;
  --bg:#e9ecee;
  --chip:#d9dee2;
}
*{box-sizing:border-box;margin:0;padding:0}
html,body{width:1200px;height:1200px;overflow:hidden}
body{background:var(--bg);font-family:"Open Sans",Arial,sans-serif;color:var(--text);position:relative}
.spread{position:absolute;left:40px;top:204px;width:1120px;height:792px;display:flex;box-shadow:0 10px 30px rgba(0,0,0,.18)}
.page{position:relative;width:560px;height:792px;background:var(--paper);overflow:hidden}
.page--inner-left{border-right:1px solid #e3e6e8}
.label{color:var(--teal);font-weight:700;font-size:12px;letter-spacing:1px;text-transform:uppercase}
.body-text{font-size:10.5px;line-height:1.55}

/* left page */
.intro{position:absolute;left:34px;top:34px;width:492px}
.intro .label{margin-bottom:10px}
.intro p{margin-bottom:8px}
.team-photo{position:absolute;left:0;top:160px;width:300px;height:150px;background:linear-gradient(135deg,#dfe6ea,#aebbc4 55%,#6f7f8a)}
.about-box{position:absolute;left:290px;top:172px;width:270px;height:128px;background:var(--teal);color:#fff;padding:18px 22px;font-size:10.5px;line-height:1.6}
.pillars{position:absolute;left:34px;top:334px;width:492px;display:grid;grid-template-columns:repeat(3,1fr);gap:22px}
.pillar h3{color:var(--teal);font-size:13px;font-weight:800;letter-spacing:1px;margin-bottom:6px}
.pillar .rule{height:3px;width:36px;background:var(--teal);margin-bottom:8px}
.promo{position:absolute;left:0;top:468px;width:560px;height:266px;background:var(--ink)}
.brand{display:flex;align-items:center;gap:8px;font-weight:800;color:#fff;font-size:15px}
.brand .dot{width:14px;height:14px;border-radius:50%;background:var(--teal);flex:0 0 14px}
.brand--stacked{position:absolute;left:26px;top:84px;width:110px;flex-direction:column;align-items:flex-start;gap:6px;font-size:14px;line-height:1.2}
.slogan{position:absolute;left:146px;top:78px;width:164px;color:#fff;font-size:16px;font-weight:700;line-height:1.3;text-align:right}
.slogan strong{color:var(--teal);font-weight:800}
.support-photo{position:absolute;left:320px;top:0;width:240px;height:266px;background:linear-gradient(160deg,#5b6b76,#2f3a42 60%,#1f272d)}
.footer-strip{position:absolute;left:0;bottom:0;width:560px;height:58px;background:var(--teal);color:#fff;font-weight:700;font-size:14px;display:flex;align-items:center;justify-content:flex-end;padding-right:30px}

/* right page */
.solutions{position:absolute;left:34px;top:30px;width:492px}
.services{margin-top:12px;display:grid;grid-template-columns:1fr 1fr;gap:18px 26px}
.service{display:flex;gap:10px}
.service svg{flex:0 0 30px}
.service h4{color:var(--teal);font-size:12.5px;font-weight:700;margin-bottom:3px}
.service p{font-size:9.5px;line-height:1.5}
.divider{position:absolute;left:34px;top:318px;width:492px;height:1px;background:#dde2e5}
.partners{position:absolute;left:34px;top:338px;width:230px}
.clients{position:absolute;left:290px;top:338px;width:236px}
.partners .label,.clients .label{text-align:center;margin-bottom:14px}
.badges{display:grid;gap:12px}
.partners .badges{grid-template-columns:repeat(3,1fr)}
.clients .badges{grid-template-columns:repeat(4,1fr)}
.badge{height:20px;border-radius:3px;background:var(--chip)}
.badge--round{border-radius:10px}
.cta{position:absolute;left:34px;top:560px;width:320px}
.cta h5{color:var(--teal);font-size:14px;font-weight:700;margin-bottom:6px}
.contact-bar{margin-top:12px;background:var(--teal);color:#fff;font-size:11px;font-weight:700;padding:8px 12px;display:flex;justify-content:space-between}
.brand--corner{position:absolute;right:34px;bottom:42px;color:var(--ink)}
</style>
</head>
<body>
<main class="spread">
  <section class="page page--inner-left">
    <div class="intro">
      <div class="label">A Empresa</div>
      <p class="body-text">Atendemos os clientes de forma consultiva, procurando no mercado as tecnologias mais adequadas para a otimização e estabilidade de redes corporativas.</p>
      <p class="body-text">Somos parceiros homologados dos principais fabricantes do mercado, além de mantermos parcerias estratégicas para complementar nossas soluções com todas as competências necessárias.</p>
    </div>
    <div class="team-photo" role="img" aria-label="Fotografia de profissionais trabalhando juntos em um escritório"></div>
    <div class="about-box">Unimos experiência técnica e atendimento próximo para entregar redes estáveis, seguras e prontas para crescer junto com o seu negócio.</div>
    <div class="pillars">
      <div class="pillar"><h3>MISSÃO</h3><div class="rule"></div><p class="body-text">Oferecer soluções de rede confiáveis que otimizem a operação dos nossos clientes.</p></div>
      <div class="pillar"><h3>VISÃO</h3><div class="rule"></div><p class="body-text">Ser referência em consultoria de redes corporativas no mercado nacional.</p></div>
      <div class="pillar"><h3>VALORES</h3><div class="rule"></div><p class="body-text">Ética, transparência, compromisso técnico e foco total no resultado do cliente.</p></div>
    </div>
    <div class="promo">
      <div class="brand brand--stacked"><span class="dot"></span><span>Horizonte &amp; Veredas</span></div>
      <p class="slogan">Somos responsáveis por <strong>SOLUCIONAR</strong> o seu problema!</p>
      <div class="support-photo" role="img" aria-label="Fotografia de técnicos em uma sala de servidores"></div>
    </div>
    <div class="footer-strip">Acesse: www.horizonteveredas.com.br</div>
  </section>

  <section class="page page--inner-right">
    <div class="solutions">
      <div class="label">Soluções</div>
      <div class="services">
        <div class="service">
          <svg width="30" height="30" viewBox="0 0 30 30"><circle cx="15" cy="15" r="13" fill="none" stroke="#2aa3b9" stroke-width="2"/><path d="M9 15l4 4 8-8" fill="none" stroke="#2aa3b9" stroke-width="2"/></svg>
          <div><h4>Troubleshooting de Redes</h4><p>Diagnóstico rápido de falhas e gargalos em redes corporativas.</p></div>
        </div>
        <div class="service">
          <svg width="30" height="30" viewBox="0 0 30 30"><circle cx="15" cy="15" r="13" fill="none" stroke="#2aa3b9" stroke-width="2"/><path d="M8 14a10 10 0 0 1 14 0M11 17a6 6 0 0 1 8 0" fill="none" stroke="#2aa3b9" stroke-width="2"/><circle cx="15" cy="20" r="1.6" fill="#2aa3b9"/></svg>
          <div><h4>Site Survey de cobertura Wi-Fi</h4><p>Medição e planejamento da cobertura sem fio do ambiente.</p></div>
        </div>
        <div class="service">
          <svg width="30" height="30" viewBox="0 0 30 30"><circle cx="15" cy="15" r="13" fill="none" stroke="#2aa3b9" stroke-width="2"/><path d="M8 18l4-5 4 3 6-7" fill="none" stroke="#2aa3b9" stroke-width="2"/></svg>
          <div><h4>Monitoramento de redes</h4><p>Acompanhamento contínuo do desempenho e da disponibilidade.</p></div>
        </div>
        <div class="service">
          <svg width="30" height="30" viewBox="0 0 30 30"><circle cx="15" cy="15" r="13" fill="none" stroke="#2aa3b9" stroke-width="2"/><rect x="9" y="10" width="12" height="4" fill="none" stroke="#2aa3b9" stroke-width="1.6"/><rect x="9" y="16" width="12" height="4" fill="none" stroke="#2aa3b9" stroke-width="1.6"/></svg>
          <div><h4>Infraestrutura</h4><p>Projeto e implantação de cabeamento e ativos de rede.</p></div>
        </div>
        <div class="service">
          <svg width="30" height="30" viewBox="0 0 30 30"><circle cx="15" cy="15" r="13" fill="none" stroke="#2aa3b9" stroke-width="2"/><path d="M11 9c-1 0-2 1-2 2 0 6 4 10 10 10 1 0 2-1 2-2l-3-2-2 1c-2-1-3-2-4-4l1-2z" fill="#2aa3b9"/></svg>
          <div><h4>Serviços de TIC</h4><p>Suporte e gestão de tecnologia da informação e comunicação.</p></div>
        </div>
        <div class="service">
          <svg width="30" height="30" viewBox="0 0 30 30"><circle cx="15" cy="15" r="13" fill="none" stroke="#2aa3b9" stroke-width="2"/><path d="M9 15h12M16 10l5 5-5 5" fill="none" stroke="#2aa3b9" stroke-width="2"/></svg>
          <div><h4>Revenda de Hardware</h4><p>Fornecimento de equipamentos dos principais fabricantes.</p></div>
        </div>
      </div>
    </div>
    <div class="divider"></div>
    <div class="partners">
      <div class="label">Parceiros</div>
      <div class="badges">
        <div class="badge badge--round"></div><div class="badge badge--round"></div><div class="badge"></div>
        <div class="badge"></div><div class="badge badge--round"></div><div class="badge"></div>
        <div class="badge"></div><div class="badge"></div><div class="badge"></div>
        <div class="badge"></div><div class="badge"></div><div class="badge"></div>
      </div>
    </div>
    <div class="clients">
      <div class="label">Clientes</div>
      <div class="badges">
        <div class="badge"></div><div class="badge badge--round"></div><div class="badge"></div><div class="badge"></div>
        <div class="badge"></div><div class="badge"></div><div class="badge badge--round"></div><div class="badge"></div>
        <div class="badge badge--round"></div><div class="badge"></div><div class="badge"></div><div class="badge"></div>
        <div class="badge"></div><div class="badge"></div><div class="badge"></div><div class="badge badge--round"></div>
      </div>
    </div>
    <div class="cta">
      <h5>Pronto para descobrir mais?</h5>
      <p class="body-text">Entre em contato e conheça as soluções ideais para a sua empresa.</p>
      <div class="contact-bar"><span>(11) 3456-0120</span><span>contato@horizonteveredas.com.br</span></div>
    </div>
    <div class="brand brand--corner"><span class="dot"></span>Horizonte &amp; Veredas</div>
  </section>
</main>
</body>
</html>
```